Marketing Brochure design required by Video Production company

We are looking for a slick, professional and eye-catching design for a marketing brochure that will showcase our company and its services.

Purpose:
The purpose of the brochure is to show our company as experienced, capable, professional and creative.

The Brochure:
The brochure will be 10 pages (including front and back cover), designed for printing in measurements of 16cm (height) x 18cm (wide).

Attached you will find:

1. Brochure Copy/Text - this is all the text to be included in the brochure. Text in red colour is not to be included in the design but is there as a guide to assist in the design

2. Design assets - our logo and hi-resolution images to be included in the design. The filenames of the images correspond with pages in the Brochure Copy/Text (as you will see)
* this does not seem to be attaching here in ArtMarketHub. Please download this file from stashbin here: https://www.stashbin.net/s/qk4tr7wnz2lpa0e/Product_Marketing_Brochure_Assets-2016-02-07.zip?dl=0

Design:
We would like the design to be open - not cramped or squashed in. Use of space is good. We want it to look very professional, but creative. And also feel simple and easy to read.

Colours to use - blues with black & white (black & white is our brand).

Please feel free to ask any questions you might have.

Thank you.

Industry/Entity Type

It Company

Font styles to use
Sans Serif

Colors
0592cd
3176b5
3276b5
33a6d7
85cae6
cee9f5
85acd3
eaf1f7

Requirements
Must have
• As per the description.
• Download design assets from:
• https://www.stashbin.net/s/qk4tr7wnz2lpa0e/Product_Marketing_Brochure_Assets-2016-02-07.zip?dl=0

```html
<!DOCTYPE html>
<html lang="en">
<head>
<meta charset="utf-8">
<title>Framelight Media – Brochure Covers</title>
<link href="https://fonts.googleapis.com/css2?family=Montserrat:wght@400;800&family=Orbitron:wght@400&family=Michroma&display=swap" rel="stylesheet">
<style>
  :root {
    --backdrop: #a3a3a8;
    --paper: #ffffff;
    --paper-cover: #e4e4e4;
    --ink: #111111;
    --ink-soft: #2a2a2a;
    --photo-dark: #8e8e8e;
    --photo-light: #d2d2d2;
    --photo-faint-a: #c9c9c9;
    --photo-faint-b: #ececec;
  }
  * { box-sizing: border-box; margin: 0; padding: 0; }
  html, body { width: 1200px; height: 1000px; overflow: hidden; }
  body { background: var(--backdrop); font-family: "Montserrat", sans-serif; }

  .spread {
    position: absolute; left: 60px; top: 260px;
    width: 1080px; height: 480px; display: flex;
    box-shadow: 0 10px 30px rgba(0,0,0,.25);
  }
  .page { position: relative; width: 540px; height: 480px; overflow: hidden; }

  /* Back cover */
  .back-cover { background: var(--paper); }
  .contact-band {
    position: absolute; left: 0; top: 105px; width: 540px; height: 260px;
    background: linear-gradient(100deg, var(--photo-light) 0%, var(--photo-dark) 55%, var(--photo-light) 100%);
  }
  .contact-heading {
    position: absolute; left: 95px; top: 118px;
    font-family: "Michroma", sans-serif; font-size: 40px; font-weight: 400;
    color: var(--ink); letter-spacing: 1px; white-space: nowrap;
  }
  .brand-name {
    font-family: "Montserrat", sans-serif; font-weight: 800; color: var(--ink);
    text-transform: uppercase; line-height: 1;
  }
  .back-cover .brand-name {
    position: absolute; left: 95px; top: 178px; font-size: 20px; letter-spacing: 4px;
  }
  .back-cover .brand-name .sub { display: block; font-size: 9px; letter-spacing: 9px; margin: 5px 0 0 48px; }
  .contact-list {
    position: absolute; left: 95px; top: 220px; list-style: none;
    font-size: 11px; color: var(--ink-soft); line-height: 18px;
  }
  .contact-list li { display: flex; align-items: center; gap: 6px; }
  .contact-list svg { width: 11px; height: 11px; fill: var(--ink-soft); }

  /* Front cover */
  .front-cover { background: var(--paper-cover); }
  .cover-photos {
    position: absolute; left: 320px; top: 70px; width: 190px; height: 380px;
    background: linear-gradient(180deg, var(--photo-faint-a), var(--photo-faint-b));
  }
  .front-cover .brand-name {
    position: absolute; left: 30px; top: 150px; font-size: 46px; letter-spacing: 7px;
  }
  .front-cover .brand-name .sub { display: block; font-size: 15px; letter-spacing: 22px; margin: 10px 0 0 170px; }
  .tagline {
    position: absolute; left: 34px; top: 262px;
    font-family: "Orbitron", sans-serif; font-size: 34px; line-height: 36px;
    color: transparent; -webkit-text-stroke: 1.2px var(--ink); letter-spacing: 3px;
  }
</style>
</head>
<body>
  <main class="spread">
    <section class="page back-cover">
      <div class="contact-band" role="img" aria-label="Black and white photo of a live event crowd and stage"></div>
      <h2 class="contact-heading">GET IN TOUCH</h2>
      <p class="brand-name">Framelight<span class="sub">Media</span></p>
      <ul class="contact-list">
        <li><svg viewBox="0 0 10 10"><path d="M5 0.5 0.5 4.5H2V9.5H8V4.5H9.5Z"/></svg>PO Box 4120 Lindale VIC 3150</li>
        <li><svg viewBox="0 0 10 10"><path d="M2 0.5 4 3 3 4.2Q4.3 6.5 5.8 7L7 6 9.5 8 8.5 9.5Q3 9 0.5 2Z"/></svg>+61 3 5550 1842</li>
        <li><svg viewBox="0 0 10 10"><path d="M0.5 2H9.5V8H0.5ZM1.2 2.6 5 5.6 8.8 2.6" stroke="#fff" stroke-width=".6"/></svg>info@framelightmedia.com.au</li>
        <li><svg viewBox="0 0 10 10"><circle cx="5" cy="5" r="4.5"/><path d="M0.5 5H9.5M5 .5V9.5" stroke="#fff" stroke-width=".6"/></svg>www.framelightmedia.com.au</li>
      </ul>
    </section>
    <section class="page front-cover">
      <div class="cover-photos" role="img" aria-label="Faded collage of video production stills"></div>
      <h1 class="brand-name">Framelight<span class="sub">Media</span></h1>
      <p class="tagline">CREATIVE<br>VIDEO<br>CONTENT</p>
    </section>
  </main>
</body>
</html>
```